Laboratory marketing Flyer

I want to create a flyer that's reflective of all the services our laboratory offers. please review our services at www.qorvantdiagnostics.com as well as about us for our amenities. focus more on areas of testing other than Toxicology, Covid-19 and Neutralizing anti-body titer. More so on UTI, Gastrointestinal, Wound, Genetics and respiratory. attached is a very old/outdated brochure, I want this in one page, vertical, front and back format.

Target Market(s)

medical facilities

Industry/Entity Type

medical

Font styles to use
Sans Serif

Colors
0054AA
0677BA
7BADD7
CADEEF
E8F1F8

Requirements
Must have
• Answer the phone, quick sample collection, fast turnaround time, large test menu, and Tarn-Ledger-Hub integration

```html
<!DOCTYPE html>
<html lang="en">
<head>
<meta charset="utf-8">
<title>Qorvant Diagnostics – Lab Flyer, Front and Back</title>
<link rel="stylesheet" href="https://fonts.googleapis.com/css2?family=Montserrat:wght@500;600;700;800;900&display=swap">
<style>
  :root {
    --brand-deep: #0054AA;
    --brand-blue: #0677BA;
    --brand-sky: #7BADD7;
    --brand-mist: #CADEEF;
    --brand-ice: #E8F1F8;
    --ring-cyan: #4cc0e4;
    --ink: #111111;
    --charcoal: #2f3033;
    --paper: #ffffff;
    --icon-ring: #3a3a3a;
    --backdrop: #6a6a6a;
  }
  * { box-sizing: border-box; margin: 0; padding: 0; }
  html, body { width: 889px; height: 1200px; overflow: hidden; background: var(--backdrop); }
  body { font-family: "Montserrat", sans-serif; position: relative; }

  .page-slot { position: absolute; top: 305px; width: 420px; height: 589px; box-shadow: 0 6px 16px rgba(0,0,0,0.35); }
  .slot-front { left: 16px; }
  .slot-back { left: 453px; }
  .page { position: absolute; left: 0; top: 0; width: 656px; height: 920px; overflow: hidden; background: var(--paper); transform: scale(0.6402); transform-origin: 0 0; }
  .page-shapes { position: absolute; inset: 0; }

  /* front */
  .brand { position: absolute; left: 0; top: 35px; width: 412px; text-align: center; }
  .brand-mark { width: 84px; height: 84px; border-radius: 50%; border: 5px solid var(--brand-deep); margin: 0 auto 14px; }
  .brand-name { color: var(--brand-deep); font-weight: 700; font-size: 27px; line-height: 1; white-space: nowrap; }

  .headline { position: absolute; left: 48px; top: 258px; font-weight: 900; font-size: 42px; line-height: 44px; color: var(--ink); }
  .headline .accent { color: var(--brand-blue); }
  .tagline { position: absolute; left: 48px; top: 405px; font-weight: 700; font-size: 14px; line-height: 20px; color: var(--ink); }

  .difference-title { position: absolute; left: 0; width: 656px; top: 498px; text-align: center; color: var(--paper); font-weight: 900; }
  .difference-title .big { display: block; font-size: 52px; line-height: 52px; }
  .difference-title .small { display: block; font-size: 29px; line-height: 32px; }

  .feature { position: absolute; width: 190px; text-align: center; color: var(--paper); font-size: 10.5px; font-weight: 500; line-height: 13px; }
  .feature-icon { width: 58px; height: 58px; margin: 0 auto 16px; border-radius: 50%; background: var(--paper); border: 3px solid var(--icon-ring); display: flex; align-items: center; justify-content: center; }
  .feature-icon svg { width: 32px; height: 32px; }

  /* back */
  .services-title { position: absolute; left: 0; width: 656px; top: 290px; text-align: center; color: var(--paper); font-weight: 800; font-size: 36px; line-height: 44px; }
  .service { position: absolute; width: 190px; text-align: center; color: var(--paper); font-size: 10.5px; font-weight: 700; line-height: 13px; text-transform: uppercase; }
  .service-icon { width: 60px; height: 60px; margin: 0 auto 15px; border-radius: 50%; background: var(--brand-blue); border: 3px solid var(--ring-cyan); display: flex; align-items: center; justify-content: center; }
  .service-icon svg { width: 32px; height: 32px; }

  /* footer, shared */
  .contact-icons { position: absolute; left: 46px; top: 865px; display: flex; flex-direction: column; gap: 6px; }
  .contact-phone { position: absolute; left: 86px; top: 862px; color: var(--brand-blue); font-weight: 800; font-size: 30px; line-height: 34px; white-space: nowrap; }
  .contact-address { position: absolute; left: 86px; top: 903px; color: var(--ink); font-weight: 600; font-size: 8.5px; line-height: 10px; white-space: nowrap; }
  .web { position: absolute; left: 410px; top: 886px; display: flex; align-items: center; gap: 8px; color: var(--paper); font-size: 12px; font-weight: 600; line-height: 20px; white-space: nowrap; }
</style>
</head>
<body>

<div class="page-slot slot-front">
<main class="page page-front">
  <svg class="page-shapes" viewBox="0 0 656 920" width="656" height="920">
    <defs>
      <linearGradient id="labPhotoTone" x1="0" y1="0" x2="1" y2="1">
        <stop offset="0" stop-color="#ffffff"/>
        <stop offset="0.5" stop-color="#E8F1F8"/>
        <stop offset="1" stop-color="#CADEEF"/>
      </linearGradient>
      <linearGradient id="labPhotoFade" x1="0" y1="0" x2="1" y2="0">
        <stop offset="0" stop-color="#ffffff"/>
        <stop offset="0.3" stop-color="#ffffff" stop-opacity="0"/>
      </linearGradient>
    </defs>
    <g role="img" aria-label="Photo of a lab scientist in cap and mask looking into a microscope">
      <rect x="300" y="0" width="356" height="540" fill="url(#labPhotoTone)"/>
      <rect x="300" y="0" width="356" height="540" fill="url(#labPhotoFade)"/>
    </g>
    <polygon points="0,532 656,405 656,920 0,920" fill="var(--brand-blue)"/>
    <rect x="0" y="870" width="656" height="50" fill="var(--charcoal)"/>
    <polygon points="0,855 356,855 392,920 0,920" fill="var(--paper)"/>
  </svg>

  <div class="brand">
    <div class="brand-mark"></div>
    <div class="brand-name">QORVANT DIAGNOSTICS</div>
  </div>

  <h1 class="headline"><span class="accent">STATE-OF-<br>THE-</span> ART LAB<br>DIAGNOSTICS</h1>
  <p class="tagline">GET FAST, PRECISE RESULTS THROUGH<br>THE MOST INNOVATIVE TESTING</p>

  <h2 class="difference-title"><span class="big">WHAT</span><span class="small">MAKES US DIFFERENT?</span></h2>

  <div class="feature" style="left:42px; top:603px;">
    <div class="feature-icon"><svg viewBox="0 0 44 44" fill="none" stroke="var(--icon-ring)" stroke-width="3"><rect x="5" y="7" width="34" height="22" rx="2"/><path d="M17 37h10M22 29v8"/><circle cx="22" cy="18" r="5" stroke="var(--brand-blue)"/></svg></div>
    Free of charge custom<br>integration<br>of our system with your EMR
  </div>
  <div class="feature" style="left:233px; top:603px;">
    <div class="feature-icon"><svg viewBox="0 0 44 44" fill="none" stroke="var(--icon-ring)" stroke-width="3"><path d="M6 8h24M10 8v24a4 4 0 0 0 8 0V8M20 8v24a4 4 0 0 0 8 0V8"/><path d="M26 24l5 5 9-11" stroke="var(--brand-blue)" stroke-width="4"/></svg></div>
    Best-in-class accuracy of<br>diagnostic test results through the<br>most innovative technology and<br>industry best-practice methods
  </div>
  <div class="feature" style="left:432px; top:603px;">
    <div class="feature-icon"><svg viewBox="0 0 44 44" fill="none" stroke="var(--icon-ring)" stroke-width="3"><circle cx="22" cy="24" r="15"/><path d="M18 5h8M22 5v4"/><path d="M15 24l5 5 10-11" stroke="var(--brand-blue)" stroke-width="4"/></svg></div>
    The gold-standard for testing<br>turnaround times
  </div>
  <div class="feature" style="left:42px; top:733px;">
    <div class="feature-icon"><svg viewBox="0 0 44 44" fill="none" stroke="var(--icon-ring)" stroke-width="3"><rect x="9" y="5" width="26" height="34" rx="2"/><path d="M14 13h16M14 19h16M14 25h16M14 31h10" stroke="var(--brand-blue)"/></svg></div>
    Customized result reports<br>for your needs
  </div>
  <div class="feature" style="left:233px; top:733px;">
    <div class="feature-icon"><svg viewBox="0 0 44 44" fill="none" stroke="var(--icon-ring)" stroke-width="3"><rect x="7" y="5" width="30" height="34" rx="2"/><path d="M12 31l7-8 5 4 8-11" stroke="var(--brand-blue)" stroke-width="3"/></svg></div>
    Reports that help providers make<br>more informed decisions based on<br>up to date comparative data
  </div>
  <div class="feature" style="left:432px; top:733px;">
    <div class="feature-icon"><svg viewBox="0 0 44 44" fill="none" stroke="var(--icon-ring)" stroke-width="3"><path d="M6 22h6v16H6zM12 24l6-10c2-3 5-1 4 2l-1 5h9c2 0 3 2 2 4l-3 9c-1 2-2 3-4 3H12"/><circle cx="32" cy="12" r="8" fill="var(--brand-blue)" stroke="none"/><path d="M32 7v10M35 9h-4a1.5 1.5 0 0 0 0 3h2a1.5 1.5 0 0 1 0 3h-4" stroke="#fff" stroke-width="1.6"/></svg></div>
    Pricing that is near-Medicare rate<br>on most diagnostic testing
  </div>

  <div class="contact-icons">
    <svg width="20" height="20" viewBox="0 0 24 24" fill="var(--ink)"><path d="M6 2l4 4-2 3c1 3 4 6 7 7l3-2 4 4-3 4C10 21 3 14 2 5z"/></svg>
    <svg width="20" height="20" viewBox="0 0 24 24" fill="none" stroke="var(--ink)" stroke-width="2.4"><path d="M12 21s-7-7-7-12a7 7 0 0 1 14 0c0 5-7 12-7 12z"/><circle cx="12" cy="9" r="2.5"/></svg>
  </div>
  <div class="contact-phone">(555) 214-3870</div>
  <div class="contact-address">4120 Lakeview Pkwy, Suite 210 Brookfield, MI 48000</div>
  <div class="web">
    <svg width="20" height="20" viewBox="0 0 26 26" fill="none" stroke="var(--brand-blue)" stroke-width="2"><circle cx="13" cy="13" r="11"/><ellipse cx="13" cy="13" rx="5" ry="11"/><path d="M2 13h22M4 7h18M4 19h18"/></svg>
    www.qorvantdiagnostics.com
  </div>
</main>
</div>

<div class="page-slot slot-back">
<section class="page page-back">
  <svg class="page-shapes" viewBox="0 0 656 920" width="656" height="920">
    <defs>
      <linearGradient id="tubePhotoTone" x1="0" y1="0" x2="1" y2="0.4">
        <stop offset="0" stop-color="#E8F1F8"/>
        <stop offset="0.35" stop-color="#f6dde5"/>
        <stop offset="0.6" stop-color="#ffffff"/>
        <stop offset="1" stop-color="#CADEEF"/>
      </linearGradient>
    </defs>
    <rect role="img" aria-label="Photo of a pipette and sample tubes in a lab" x="0" y="0" width="656" height="310" fill="url(#tubePhotoTone)"/>
    <polygon points="0,300 656,210 656,920 0,920" fill="var(--brand-blue)"/>
    <rect x="0" y="870" width="656" height="50" fill="var(--charcoal)"/>
    <polygon points="0,855 356,855 392,920 0,920" fill="var(--paper)"/>
  </svg>

  <h2 class="services-title">OUR SERVICES</h2>

  <div class="service" style="left:38px; top:355px;">
    <div class="service-icon"><svg viewBox="0 0 32 32" fill="none" stroke="#fff" stroke-width="2.6"><path d="M7 6h8M18 6h8M9 6v16a2 2 0 0 0 4 0V6M20 6v16a2 2 0 0 0 4 0V6"/></svg></div>
    Blood Department
  </div>
  <div class="service" style="left:229px; top:355px;">
    <div class="service-icon"><svg viewBox="0 0 32 32" fill="#fff"><rect x="4" y="7" width="9" height="18" rx="4.5"/><circle cx="22" cy="18" r="7"/><path d="M17 22l10-8" stroke="var(--brand-blue)" stroke-width="2"/></svg></div>
    Toxicology Testing
  </div>
  <div class="service" style="left:429px; top:355px;">
    <div class="service-icon"><svg viewBox="0 0 32 32" fill="#fff" stroke="#fff" stroke-width="2"><circle cx="16" cy="16" r="7"/><path d="M16 4v5M16 23v5M4 16h5M23 16h5M7.5 7.5l3.5 3.5M21 21l3.5 3.5M7.5 24.5l3.5-3.5M21 11l3.5-3.5"/></svg></div>
    COVID-19 Testing
  </div>

  <div class="service" style="left:38px; top:464px;">
    <div class="service-icon"><svg viewBox="0 0 32 32" fill="#fff"><path d="M14 6v10c-2 0-7 2-9 8-1 3 1 4 4 3 3-1 5-3 5-6zM18 6v10c2 0 7 2 9 8 1 3-1 4-4 3-3-1-5-3-5-6z"/></svg></div>
    Respiratory Pathogen<br>Panel (RPP)
  </div>
  <div class="service" style="left:229px; top:464px;">
    <div class="service-icon"><svg viewBox="0 0 32 32" fill="#fff"><rect x="8" y="5" width="16" height="4" rx="1"/><path d="M10 11h12l-1 16H11z"/><path d="M12 15h6M12 19h6M12 23h6" stroke="var(--brand-blue)" stroke-width="1.6"/></svg></div>
    Urinary Tract<br>Infection qPCR
  </div>
  <div class="service" style="left:429px; top:464px;">
    <div class="service-icon"><svg viewBox="0 0 32 32" fill="none" stroke="#fff" stroke-width="3"><circle cx="16" cy="12" r="6"/><path d="M16 18v10M12 24h8"/></svg></div>
    Women's Health qPCR
  </div>

  <div class="service" style="left:38px; top:585px;">
    <div class="service-icon"><svg viewBox="0 0 32 32" fill="#fff"><circle cx="11" cy="12" r="5"/><circle cx="22" cy="20" r="4"/><path d="M11 4v16M3 12h16M16 20h12M22 14v12" stroke="#fff" stroke-width="2"/></svg></div>
    Sexually Transmitted<br>Infections (STI)
  </div>
  <div class="service" style="left:229px; top:585px;">
    <div class="service-icon"><svg viewBox="0 0 32 32" fill="none" stroke="#fff" stroke-width="3" stroke-linecap="round"><path d="M14 4v6c-6 0-8 4-8 8 0 5 4 8 9 8 5 0 10-3 10-9 0-4-3-6-6-5-2 1-2 4 0 4"/></svg></div>
    Gastrointestinal Panel
  </div>
  <div class="service" style="left:429px; top:585px;">
    <div class="service-icon"><svg viewBox="0 0 32 32" fill="#fff"><circle cx="11" cy="11" r="6"/><circle cx="21" cy="21" r="6"/><circle cx="22" cy="9" r="3"/><circle cx="9" cy="23" r="3"/></svg></div>
    Infectious Diseases
  </div>

  <div class="service" style="left:38px; top:701px;">
    <div class="service-icon"><svg viewBox="0 0 32 32" fill="#fff"><rect x="3" y="11" width="26" height="10" rx="3"/><rect x="12" y="13" width="8" height="6" fill="var(--brand-blue)"/></svg></div>
    Wound Panel
  </div>
  <div class="service" style="left:229px; top:701px;">
    <div class="service-icon"><svg viewBox="0 0 32 32" fill="#fff"><rect x="9" y="6" width="3" height="12" rx="1.5"/><rect x="13" y="4" width="3" height="14" rx="1.5"/><rect x="17" y="5" width="3" height="13" rx="1.5"/><rect x="21" y="8" width="3" height="11" rx="1.5"/><path d="M8 16h16v4c0 5-3 8-8 8-4 0-6-3-8-6l-3-5 2-1 3 3z"/></svg></div>
    Nail Panel
  </div>
  <div class="service" style="left:429px; top:701px;">
    <div class="service-icon"><svg viewBox="0 0 32 32" fill="none" stroke="#fff" stroke-width="3"><path d="M8 4h16M8 28h16M10 4c0 8 12 16 12 24M22 4c0 8-12 16-12 24"/></svg></div>
    Genetic Testing
  </div>

  <div class="contact-icons">
    <svg width="20" height="20" viewBox="0 0 24 24" fill="var(--ink)"><path d="M6 2l4 4-2 3c1 3 4 6 7 7l3-2 4 4-3 4C10 21 3 14 2 5z"/></svg>
    <svg width="20" height="20" viewBox="0 0 24 24" fill="none" stroke="var(--ink)" stroke-width="2.4"><path d="M12 21s-7-7-7-12a7 7 0 0 1 14 0c0 5-7 12-7 12z"/><circle cx="12" cy="9" r="2.5"/></svg>
  </div>
  <div class="contact-phone">(555) 214-3870</div>
  <div class="contact-address">4120 Lakeview Pkwy, Suite 210 Brookfield, MI 48000</div>
  <div class="web">
    <svg width="20" height="20" viewBox="0 0 26 26" fill="none" stroke="var(--brand-blue)" stroke-width="2"><circle cx="13" cy="13" r="11"/><ellipse cx="13" cy="13" rx="5" ry="11"/><path d="M2 13h22M4 7h18M4 19h18"/></svg>
    www.qorvantdiagnostics.com
  </div>
</section>
</div>

</body>
</html>
```